Harbor of Mercy - Team of Rabbis and Doctors Helping Families Dealing with Illness

The Harbor of Mercy is an organization that accompanies families dealing with severe illnesses of a family member. A team of rabbis and doctors provide support and real-time responses to these families.
The site theme is medicine and law, but the target market is religious Jewish families in crisis. Thus, the site design needs to combine:
- professional, conservative, serious
- spiritual
- warm hug

Target Market(s)

religious families suffering a health crisis

Industry/Entity Type

Non-profit organization

Number of Pages Required

1 page

Font styles to use
Sans Serif

Requirements
Must have
• Final design in PSD format. List of fonts used, colors used and link/button colors used in the design.

```html
<!DOCTYPE html>
<html lang="en">
<head>
<meta charset="utf-8">
<title>The Harbor of Mercy</title>
<link href="https://fonts.googleapis.com/css2?family=Poppins:wght@500;600;700;800&family=Lato:wght@400;700&display=swap" rel="stylesheet">
<style>
:root{
  --teal:#14a3a6;
  --teal-dark:#0e8a8d;
  --orange:#ef9a1f;
  --ink:#1c1c1c;
  --navy:#122636;
  --footer:#2b2d30;
  --light:#f4f5f6;
  --white:#ffffff;
}
*{box-sizing:border-box;margin:0;padding:0}
html,body{width:1200px;height:3968px;overflow:hidden}
body{font-family:"Lato",sans-serif;color:var(--ink);background:var(--white);position:relative}
.abs{position:absolute}
h2.section-title{font-family:"Poppins",sans-serif;font-weight:800;font-size:32px;text-align:center;letter-spacing:.5px}

/* top bar */
.topbar{left:0;top:0;width:1200px;height:40px;background:var(--teal)}
.search{left:145px;top:7px;width:142px;height:26px;background:#fff;border-radius:2px;font-size:13px;padding:5px 6px;color:#333}
.top-icon{top:6px;width:28px;height:28px;border:2px solid #fff;border-radius:50%}
.hotline{left:373px;top:10px;color:#fff;font-family:"Poppins",sans-serif;font-weight:600;font-size:15px}

/* nav */
.nav{left:0;top:40px;width:1200px;height:102px;background:#fff}
.nav ul{position:absolute;left:145px;top:38px;display:flex;gap:32px;list-style:none;font-family:"Poppins",sans-serif;font-weight:600;font-size:16px}
.brand{right:140px;top:34px;display:flex;align-items:center;gap:10px;font-family:"Poppins",sans-serif;font-weight:800;font-size:24px;color:var(--orange)}
.brand .mark{width:22px;height:22px;background:var(--teal);border-radius:50%}

/* hero */
.hero{left:0;top:142px;width:1200px;height:536px;background:linear-gradient(100deg,#ece9e4 0%,#d9d3cb 40%,#6b5a4e 65%,#2c2624 100%);overflow:hidden}
.pill{left:0;height:96px;border-radius:0 48px 48px 0;border:4px solid rgba(255,255,255,.25);display:flex;align-items:center;font-family:"Poppins",sans-serif;font-weight:800;font-size:32px;line-height:1.1;color:var(--ink);overflow:hidden;white-space:nowrap}
.pill.orange{top:138px;width:578px;background:var(--orange);padding-left:42px}
.pill.teal{width:195px;background:var(--teal);justify-content:flex-end;padding-right:30px}

/* about */
.about-left{left:0;top:678px;width:600px;height:552px;background:var(--orange)}
.about-right{left:600px;top:678px;width:600px;height:552px;background:var(--teal)}
.about-head{top:30px;width:600px;text-align:center;color:#fff;font-family:"Poppins",sans-serif;font-weight:800;font-size:32px}
.video{left:28px;top:96px;width:544px;height:400px;border:4px solid #fff;background:linear-gradient(135deg,#5f6d73,#a7b0b3 55%,#e1e4e4);display:flex;align-items:center;justify-content:center}
.about-card{left:28px;top:96px;width:544px;height:400px;background:#fff;padding:24px 16px;text-align:center;font-size:14.5px;line-height:1.55;color:#333}
.about-card p{margin-bottom:10px}
.btn{display:inline-block;background:var(--orange);color:#1c1c1c;font-size:16px;padding:10px 24px;border-radius:3px;margin-top:14px}

/* gallery */
.gallery{left:0;top:1270px;width:1200px;height:672px;background:var(--light)}
.gallery h2{position:absolute;top:52px;width:1200px}
.shot{border:4px solid #fff;box-shadow:0 4px 14px rgba(0,0,0,.18)}

/* teasers */
.teasers{left:0;top:1943px;width:1200px;height:577px;background:linear-gradient(180deg,#0d1e2b,#1e3a4e 50%,#0c1b27)}
.teaser{top:0;width:285px;color:#fff;text-align:center}
.teaser h3{margin-top:72px;font-family:"Poppins",sans-serif;font-weight:800;font-size:30px}
.teaser .photo{margin-top:12px;height:257px;border:2px solid #dfe4e8;background:linear-gradient(135deg,#8c8f90,#d7d2cb)}
.teaser h4{margin-top:24px;font-family:"Poppins",sans-serif;font-weight:700;font-size:24px}
.teaser p{margin-top:6px;font-size:13.5px;line-height:1.6;padding:0 4px}

/* testimonials */
.testimonials{left:0;top:2520px;width:1200px;height:530px;background:#fff}
.testimonials h2{position:absolute;top:42px;width:1200px}
.review{top:130px;width:308px;text-align:center}
.stars{display:flex;justify-content:center;gap:8px;height:26px}
.bubble{margin-top:14px;height:200px;background:#fff;border-radius:18px;box-shadow:0 4px 16px rgba(0,0,0,.16);padding:26px 14px;font-size:13px;line-height:1.75;color:#333;position:relative}
.bubble::after{content:"";position:absolute;left:50%;bottom:-40px;margin-left:-22px;border:22px solid transparent;border-top:20px solid #fff;border-bottom:0;border-top-width:40px}
.review.featured .bubble{background:var(--teal);color:#fff}
.review.featured .bubble::after{border-top-color:var(--teal)}
.who{margin-top:56px;font-family:"Poppins",sans-serif;font-weight:600;font-size:17px;line-height:1.35}

/* news */
.news{left:0;top:3050px;width:1200px;height:542px;background:linear-gradient(180deg,#11a0a3,#0c7f83)}
.news h2{position:absolute;top:42px;width:1200px;color:#fff}
.story{top:117px;width:285px;color:#fff;text-align:center}
.story .photo{height:258px;border:2px solid #fff;background:linear-gradient(135deg,#7c8a92,#d6d9da)}
.story h4{margin-top:26px;font-family:"Poppins",sans-serif;font-weight:700;font-size:24px;color:#fff}
.story p{margin-top:6px;font-size:13.5px;line-height:1.6}

/* footer */
.footer{left:0;top:3592px;width:1200px;height:376px;background:var(--footer);color:#fff}
.foot-brand{left:145px;top:118px;display:flex;align-items:center;gap:10px;font-family:"Poppins",sans-serif;font-weight:800;font-size:24px;color:#fff}
.foot-brand .mark{width:22px;height:22px;background:var(--teal);border-radius:50%}
.foot-col h5{font-family:"Poppins",sans-serif;font-weight:600;font-size:21px;margin-bottom:10px}
.foot-col li{list-style:none;font-family:"Poppins",sans-serif;font-weight:600;font-size:15px;line-height:1.7}
.contact-row{display:flex;gap:12px;align-items:flex-start;font-family:"Poppins",sans-serif;font-weight:600;font-size:15px;line-height:1.3;margin-bottom:14px}
.contact-row svg{flex:none}
.field{width:228px;height:36px;background:#fff;color:#222;font-size:14px;padding:9px 10px;margin-bottom:12px;border:1px solid #ccc}
.subscribe{display:inline-block;background:var(--orange);color:#fff;font-size:14px;padding:9px 14px;border-radius:18px}
.rule{left:145px;top:312px;width:910px;height:1px;background:#5e6064}
.copyright{top:334px;width:1200px;text-align:center;font-family:"Poppins",sans-serif;font-weight:600;font-size:14px}
</style>
</head>
<body>

<!-- top bar -->
<div class="abs topbar">
  <div class="abs search">Search</div>
  <div class="abs top-icon" style="left:298px"></div>
  <div class="abs top-icon" style="left:338px">
    <svg width="24" height="24" viewBox="0 0 24 24"><path d="M8 6l2 3-1.5 1.5c.8 1.8 2.2 3.2 4 4L14 13l3 2-1 2.5c-4 0-9-5-9-9z" fill="none" stroke="#fff" stroke-width="1.6"/></svg>
  </div>
  <div class="abs hotline">+1 555 010 2030 &nbsp;/&nbsp; 24/7 Hotline</div>
</div>

<!-- navigation -->
<div class="abs nav">
  <ul><li>HOME</li><li>ABOUT US</li><li>VIDEOS</li><li>TESTIMONIALS</li><li>NEWS</li><li>CONTACT</li></ul>
  <div class="abs brand"><span class="mark"></span>Harbor of Mercy</div>
</div>

<!-- hero -->
<div class="abs hero" role="img" aria-label="A father and son reading a holy book beside lit candles">
  <div class="abs pill orange">SHOULD MORPHINE BE GIVEN<br>TO THE PATIENT?</div>
  <div class="abs pill teal" style="top:258px">E PATIENT<br>ATED?</div>
  <div class="abs pill teal" style="top:378px">PATIENTS<br>TMENT?</div>
</div>

<!-- about -->
<div class="abs about-left">
  <div class="abs about-head">ABOUT US</div>
  <div class="abs video" role="img" aria-label="Video still of an elderly patient speaking with a doctor">
    <svg width="80" height="80" viewBox="0 0 80 80"><circle cx="40" cy="40" r="35" fill="none" stroke="#fff" stroke-width="5"/><path d="M32 24l22 16-22 16z" fill="#fff"/></svg>
  </div>
</div>
<div class="abs about-right">
  <div class="abs about-head">ABOUT US</div>
  <div class="abs about-card">
    <p>Duis aute irure dolor in reprehenderit in voluptate velit esse cillum dolore eu fugiat nulla pariatur. Excepteur sint occaecat cupidatat non proident, sunt in culpa qui officia deserunt mollit anim id est laborum.</p>
    <p>Nemo enim ipsam voluptatem quia voluptas sit aspernatur aut odit aut fugit, sed quia consequuntur magni dolores eos qui ratione voluptatem sequi nesciunt. Neque porro quisquam est, qui dolorem ipsum quia dolor sit amet, consectetur, adipisci velit, sed quia non numquam eius modi tempora incidunt ut labore et dolore magnam aliquam quaerat voluptatem.</p>
    <p>Duis aute irure dolor in reprehenderit in voluptate velit esse cillum dolore eu fugiat nulla pariatur. Excepteur sint occaecat cupidatat non proident, sunt in culpa qui officia deserunt mollit anim id est laborum.</p>
    <span class="btn">Read More</span>
  </div>
</div>

<!-- gallery -->
<div class="abs gallery">
  <h2 class="section-title">IMAGE GALLERY</h2>
  <div class="abs shot" style="left:16px;top:200px;width:250px;height:320px;background:linear-gradient(135deg,#5a4a40,#e8e6e2)" role="img" aria-label="Doctor reviewing notes with a patient"></div>
  <div class="abs shot" style="left:934px;top:200px;width:250px;height:320px;background:linear-gradient(135deg,#d8d4cf,#4c6a88)" role="img" aria-label="Nurse walking arm in arm with an elderly woman"></div>
  <div class="abs shot" style="left:256px;top:130px;width:684px;height:457px;background:linear-gradient(120deg,#f3f1ec,#c9d3da 45%,#3d6d9c 75%,#e2c14b)" role="img" aria-label="Nurse with a tablet talking with a senior patient"></div>
</div>

<!-- teasers -->
<div class="abs teasers">
  <div class="abs teaser" style="left:13px"><h3>TEASER 1</h3><div class="photo" role="img" aria-label="Group of adults studying together at a table"></div><h4>COURSES</h4><p>Excepteur sint occaecat cupidatat non proi dent, sunt in culpa qui deserunt mollit anim id est laborum.</p></div>
  <div class="abs teaser" style="left:309px"><h3>TEASER 2</h3><div class="photo" role="img" aria-label="Presenter speaking to a seated audience in a conference room"></div><h4>CONFERENCES</h4><p>Excepteur sint occaecat cupidatat non proi dent, sunt in culpa qui deserunt mollit anim id est laborum.</p></div>
  <div class="abs teaser" style="left:605px"><h3>TEASER 3</h3><div class="photo" role="img" aria-label="Lecturer addressing a full auditorium"></div><h4>LECTURES</h4><p>Excepteur sint occaecat cupidatat non proi dent, sunt in culpa qui deserunt mollit anim id est laborum.</p></div>
  <div class="abs teaser" style="left:901px"><h3>TEASER 4</h3><div class="photo" role="img" aria-label="Support line operators wearing headsets"></div><h4>HOTLINE 24/7</h4><p>Excepteur sint occaecat cupidatat non proi dent, sunt in culpa qui deserunt mollit anim id est laborum.</p></div>
</div>

<!-- testimonials -->
<div class="abs testimonials">
  <h2 class="section-title">TESTIMONIALS</h2>
  <svg width="0" height="0" style="position:absolute"><defs><path id="star" d="M12 1.5l3.2 7 7.6.8-5.7 5.1 1.6 7.5L12 18l-6.7 3.9 1.6-7.5L1.2 9.3l7.6-.8z"/></defs></svg>
  <div class="abs review" style="left:110px">
    <div class="stars"><svg width="26" height="26" viewBox="0 0 24 24"><use href="#star" fill="#444"/></svg><svg width="26" height="26" viewBox="0 0 24 24"><use href="#star" fill="#444"/></svg><svg width="26" height="26" viewBox="0 0 24 24"><use href="#star" fill="#444"/></svg><svg width="26" height="26" viewBox="0 0 24 24"><use href="#star" fill="#444"/></svg><svg width="26" height="26" viewBox="0 0 24 24"><use href="#star" fill="#444"/></svg></div>
    <div class="bubble">Lorem ipsum dolor sit amet, consectetur adipiscing elit, sed do eiusmod tempor incididunt ut labore et dolore magna aliqua. Ut enim ad minim veniam, quis nostrud exercitation ullamco laboris nisi ut aliquip ex ea commodo consequat.</div>
    <div class="who">MIRIAM ADLER<br>3/23/2023</div>
  </div>
  <div class="abs review featured" style="left:445px">
    <div class="stars"><svg width="26" height="26" viewBox="0 0 24 24"><use href="#star" fill="#14a3a6"/></svg><svg width="26" height="26" viewBox="0 0 24 24"><use href="#star" fill="#14a3a6"/></svg><svg width="26" height="26" viewBox="0 0 24 24"><use href="#star" fill="#14a3a6"/></svg><svg width="26" height="26" viewBox="0 0 24 24"><use href="#star" fill="#14a3a6"/></svg><svg width="26" height="26" viewBox="0 0 24 24"><use href="#star" fill="#14a3a6"/></svg></div>
    <div class="bubble">Lorem ipsum dolor sit amet, consectetur adipiscing elit, sed do eiusmod tempor incididunt ut labore et dolore magna aliqua. Ut enim ad minim veniam, quis nostrud exercitation ullamco laboris nisi ut aliquip ex ea commodo consequat.</div>
    <div class="who">RACHEL STERN<br>3/23/2023</div>
  </div>
  <div class="abs review" style="left:781px">
    <div class="stars"><svg width="26" height="26" viewBox="0 0 24 24"><use href="#star" fill="#444"/></svg><svg width="26" height="26" viewBox="0 0 24 24"><use href="#star" fill="#444"/></svg><svg width="26" height="26" viewBox="0 0 24 24"><use href="#star" fill="#444"/></svg><svg width="26" height="26" viewBox="0 0 24 24"><use href="#star" fill="#444"/></svg><svg width="26" height="26" viewBox="0 0 24 24"><use href="#star" fill="#444"/></svg></div>
    <div class="bubble">Lorem ipsum dolor sit amet, consectetur adipiscing elit, sed do eiusmod tempor incididunt ut labore et dolore magna aliqua. Ut enim ad minim veniam, quis nostrud exercitation ullamco laboris nisi ut aliquip ex ea commodo consequat.</div>
    <div class="who">DINA WEISS<br>3/23/2023</div>
  </div>
</div>

<!-- news -->
<div class="abs news">
  <h2 class="section-title">LATEST NEWS</h2>
  <div class="abs story" style="left:145px"><div class="photo" role="img" aria-label="Colleagues laughing together over papers"></div><h4>NEMO ENIM IPSAM</h4><p>Excepteur sint occaecat cupidatat non proi dent, sunt in culpa qui deserunt mollit anim id est laborum.</p></div>
  <div class="abs story" style="left:457px"><div class="photo" role="img" aria-label="Smiling nurse in front of a medical team"></div><h4>SED UT PERSPICIATIS</h4><p>Excepteur sint occaecat cupidatat non proi dent, sunt in culpa qui deserunt mollit anim id est laborum.</p></div>
  <div class="abs story" style="left:769px"><div class="photo" role="img" aria-label="Doctors meeting around a table"></div><h4>MAGNI DOLORES</h4><p>Excepteur sint occaecat cupidatat non proi dent, sunt in culpa qui deserunt mollit anim id est laborum.</p></div>
</div>

<!-- footer -->
<div class="abs footer">
  <div class="abs foot-brand"><span class="mark"></span>Harbor of Mercy</div>
  <div class="abs foot-col" style="left:397px;top:78px">
    <h5>Quick Links</h5>
    <ul><li>Home</li><li>About Us</li><li>Services</li><li>News</li><li>Contact Us</li></ul>
  </div>
  <div class="abs foot-col" style="left:565px;top:78px;width:250px">
    <h5>Contact Us</h5>
    <div class="contact-row"><svg width="30" height="30" viewBox="0 0 30 30"><circle cx="15" cy="15" r="15" fill="#fff"/><rect x="8" y="10" width="14" height="10" fill="none" stroke="#2b2d30" stroke-width="1.6"/><path d="M8 10l7 6 7-6" fill="none" stroke="#2b2d30" stroke-width="1.6"/></svg><span style="padding-top:5px">hello@harborofmercy.org</span></div>
    <div class="contact-row"><svg width="30" height="30" viewBox="0 0 30 30"><circle cx="15" cy="15" r="15" fill="#fff"/><path d="M15 23s-6-6-6-10a6 6 0 0112 0c0 4-6 10-6 10z" fill="none" stroke="#2b2d30" stroke-width="1.6"/><circle cx="15" cy="13" r="2" fill="#2b2d30"/></svg><span>18 Cedar Lane Brooklyn,<br>New York</span></div>
    <div class="contact-row"><svg width="30" height="30" viewBox="0 0 30 30"><circle cx="15" cy="15" r="15" fill="#fff"/><path d="M10 8l3 4-2 2c1 2.2 2.8 4 5 5l2-2 4 3-1.5 3C14 23 7 16 7 10z" fill="#2b2d30"/></svg><span style="padding-top:5px">555 010 2030</span></div>
  </div>
  <div class="abs foot-col" style="left:825px;top:78px">
    <h5>Contact Form</h5>
    <div class="field">Name</div>
    <div class="field">Email Address</div>
    <span class="subscribe">Subscribe</span>
  </div>
  <div class="abs rule"></div>
  <div class="abs copyright">Copyrights @ 2023. &nbsp;All Rights Reserved.</div>
</div>

</body>
</html>
```